Fast Money - Simple Book Cover Design

Hello,

I am in need of a cover for my new book. The Book Title Is

"Standing Growth - Keys to Glowing Customer Ratings That Fill The Calendar and Draw Fresh Clients Through Every Entrance!"

Author: Fireman Dale Orsworth

What I want: This is a book for businesses on improving their online reputation. I want to have 5 Stars on the cover. You can look at this quarvex search for ideas of what I am meaning.....

(copy and paste)

http://www.quarvex-find.example/search?q=5+star+online+reviews&mode=images&ref=kx7Lp2QwZt9 (copy and paste)

I am open to different color schemes for the book. I am partial to dark blues if you make it look good. Here is another book that I really like the cover of....

http://www.brindlemart.example/Clipwave-Tactics-Earning-Promotion-ebook/item/Z93KT4WQPX

I want the cover BOLD and to STAND OUT.

I am looking for a design to help establish me as an authority for online reputation marketing. This book will be both in Pagely format and be used in print as well.

I am open to questions....

Thanks!

Dale

Reason: I don't believe we have received the right designs. I am going to give everyone more time...

Reason: Hi everyone, I had some stuff come up and was not able to be involved in this project. I am extending because we have not seen the exact thing we want and need time to work with designers to get it right. Thanks Dale

Reason: I am currently traveling and can't wrap this up until I get back.

Target Market(s)

Business Owners

Industry/Entity Type

Business

Requirements
Must have
• Title and Subtitle

Author Name

5 Stars Images....
Nice to have
• Creativity

Bold and stand out

Professional

Should not have
• thin text, small to read text, lame graphics,

```html
<!DOCTYPE html>
<html lang="en">
<head>
<meta charset="utf-8">
<title>Standing Growth – Book Cover</title>
<link href="https://fonts.googleapis.com/css2?family=Archivo+Black&family=Arimo:wght@700&display=swap" rel="stylesheet">
<style>
  :root {
    --magenta: #b60652;
    --wine: #7d1116;
    --gold: #f5b836;
    --rule: #f2c23a;
    --ink: #111111;
    --white: #ffffff;
  }
  * { margin: 0; padding: 0; box-sizing: border-box; }
  html, body { width: 900px; height: 1200px; overflow: hidden; background: var(--wine); }
  .cover {
    position: relative;
    width: 900px;
    height: 1200px;
    overflow: hidden;
    background: linear-gradient(to bottom, var(--magenta) 0 597px, var(--wine) 597px 100%);
  }
  .author-plate {
    position: absolute;
    left: 100px;
    top: 0;
    width: 710px;
    height: 120px;
    background: var(--gold);
    display: flex;
    align-items: center;
    justify-content: center;
  }
  .author-name {
    font-family: "Archivo Black", "Arial Black", sans-serif;
    font-size: 44px;
    color: var(--ink);
    letter-spacing: 0.5px;
    padding-top: 4px;
  }
  .title {
    position: absolute;
    left: 0;
    top: 150px;
    width: 900px;
    text-align: center;
    font-family: "Arimo", Arial, sans-serif;
    font-weight: 700;
    font-size: 146px;
    line-height: 140px;
    color: var(--white);
    letter-spacing: 1px;
  }
  .title-rule {
    position: absolute;
    top: 303px;
    height: 3px;
    background: var(--rule);
  }
  .title-rule.left { left: 0; width: 62px; }
  .title-rule.right { right: 0; width: 68px; }
  .stars {
    position: absolute;
    left: 100px;
    top: 536px;
    width: 700px;
    height: 130px;
  }
  .subtitle {
    position: absolute;
    right: 98px;
    top: 760px;
    text-align: right;
    font-family: "Archivo Black", "Arial Black", sans-serif;
    font-size: 45px;
    line-height: 67px;
    color: var(--white);
  }
</style>
</head>
<body>
  <main class="cover">
    <div class="author-plate">
      <p class="author-name">Fireman Dale Orsworth</p>
    </div>

    <h1 class="title">Standing<br>Growth</h1>
    <span class="title-rule left"></span>
    <span class="title-rule right"></span>

    <svg class="stars" viewBox="0 0 700 130" aria-label="Five star rating">
      <defs>
        <radialGradient id="star-fill" cx="50%" cy="40%" r="60%">
          <stop offset="0%" stop-color="#fff6b0"/>
          <stop offset="45%" stop-color="#ffd23a"/>
          <stop offset="100%" stop-color="#e79a0c"/>
        </radialGradient>
        <polygon id="star" points="0,-62 14.6,-20.1 59,-19.2 23.6,7.7 36.4,50.2 0,25 -36.4,50.2 -23.6,7.7 -59,-19.2 -14.6,-20.1"
                 fill="url(#star-fill)" stroke="#8a4a05" stroke-width="2.5" stroke-linejoin="round"/>
      </defs>
      <use href="#star" x="72" y="68"/>
      <use href="#star" x="211" y="68"/>
      <use href="#star" x="350" y="68"/>
      <use href="#star" x="489" y="68"/>
      <use href="#star" x="628" y="68"/>
    </svg>

    <p class="subtitle">
      Keys to Glowing<br>
      Customer Ratings That<br>
      Fill The Calendar and<br>
      Draw Fresh Clients<br>
      Through Every Entrance!
    </p>
  </main>
</body>
</html>
```